Label Design DormaLux Capsules

Hello dear designers!

We run a brand for dietary supplements and are looking for a talented designer to help take our brand to the next level. We are planning to launch new products with fresh packaging and redesigned labels. Additionally, we would like to refresh our company logo to make it fit better on the packaging.

Important Info:

Our brand: PuraVeta – specializing in products for detoxification, sleep, and eye protection.
Our shop: www.puraveta-shop.at – currently offering two main products:
PuraVeta (Detox Tincture)
Ocula Shield Guard (Blue Light Filter Glasses)
Project Goal: Initially, we are looking for a label design for our new product DormaLux (sleep capsules). If we like the design, we would like to revise the label for our first product, PuraVeta, and potentially rework our logo to make it more compact and visually appealing on our packaging.

Design Preferences: We are fans of the design style of Varo Nutra and would love a design in a similar style – modern, clean, and premium – but with a unique touch that fits our brand. You will find some inspirations and ideas that we particularly like in the attachment.

Important:

Our packaging for DormaLux is an 8 OZ jar (similar to the smaller jars used by Varo Nutra).
The label should be clear, appealing, and give the product a high-quality look.
An example of a previous design draft (which hasn’t fully convinced us yet), along with inspirations for our upcoming bundle (including PuraVeta, DormaLux, and OculaShield Guard), is also attached.
Special Opportunity: The designer with the best concept will have the chance to collaborate with us long-term! We have two more brands in the pipeline and are looking for a reliable and creative partner for future projects. Generous compensation and tips are guaranteed.

We look forward to seeing creative and professional designs that will take our brand to the next level!

Target Market(s)

Germany

Industry/Entity Type

Supplement

Font styles to use
Sans Serif

Colors

Designer to choose colors to be used in the design.

Requirements
Must have
• Es sollte Hochwertig und Modern aussehen. Matt schwarzer hintergrund. less is more
Nice to have
• Maybe The head should be visible in the background.
Should not have
• it should not be colorful, and not too playful, it should definitely not look cheap!

```html
<!DOCTYPE html>
<html lang="de">
<head>
<meta charset="utf-8">
<title>DormaLux – Etikett</title>
<link rel="stylesheet" href="https://fonts.googleapis.com/css2?family=Barlow+Condensed:wght@500;600&family=Montserrat:wght@500&display=swap">
<style>
  :root {
    --backdrop: #e4e4e4;
    --label: #2b2b2b;
    --label-edge: #232323;
    --tab: #1f1f1f;
    --white: #f4f4f4;
    --cyan: #2bb5e6;
    --gold: #c59a63;
    --gold-soft: rgba(197, 154, 99, 0.14);
    --head-soft: rgba(0, 0, 0, 0.22);
  }
  * { margin: 0; padding: 0; box-sizing: border-box; }
  html, body { width: 1200px; height: 1200px; overflow: hidden; }
  body {
    background: var(--backdrop);
    display: flex;
    align-items: center;
    justify-content: center;
    font-family: "Barlow Condensed", sans-serif;
  }
  .label {
    position: relative;
    width: 900px;
    height: 1000px;
    background: linear-gradient(180deg, var(--label) 0%, var(--label-edge) 100%);
    border-radius: 6px;
    overflow: hidden;
  }
  .brand-tab {
    position: absolute;
    top: 0;
    left: 50%;
    transform: translateX(-50%);
    width: 300px;
    height: 190px;
    background: var(--tab);
    border-radius: 0 0 150px 150px;
    display: flex;
    flex-direction: column;
    align-items: center;
    padding-top: 70px;
    gap: 18px;
  }
  .brand-name {
    font-family: "Montserrat", sans-serif;
    font-weight: 500;
    font-size: 17px;
    letter-spacing: 5px;
    color: var(--gold);
  }
  .brand-dot {
    width: 30px;
    height: 30px;
    border-radius: 50%;
    border: 2px solid var(--gold);
  }
  .head-backdrop {
    position: absolute;
    left: 230px;
    top: 260px;
    width: 440px;
    height: 560px;
    border-radius: 48% 48% 30% 30%;
    background: radial-gradient(ellipse at center, var(--head-soft) 0%, transparent 70%);
  }
  .network {
    position: absolute;
    width: 220px;
    height: 460px;
    top: 380px;
    background: radial-gradient(ellipse at center, var(--gold-soft) 0%, transparent 70%);
  }
  .network.left { left: 20px; }
  .network.right { right: 20px; }
  .content {
    position: absolute;
    top: 330px;
    left: 0;
    width: 100%;
    display: flex;
    flex-direction: column;
    align-items: center;
  }
  .product-name {
    font-weight: 600;
    font-size: 156px;
    line-height: 1;
    color: var(--white);
    letter-spacing: 2px;
  }
  .claim {
    margin-top: 22px;
    padding: 10px 46px;
    border: 3px solid var(--cyan);
    border-radius: 40px;
    font-weight: 600;
    font-size: 42px;
    letter-spacing: 0.5px;
    color: var(--cyan);
  }
  .benefits {
    margin-top: 42px;
    margin-left: 110px;
    list-style: none;
    display: flex;
    flex-direction: column;
    gap: 12px;
  }
  .benefits li {
    font-weight: 600;
    font-size: 30px;
    color: var(--white);
    padding-left: 10px;
    border-left: 2px solid var(--cyan);
    line-height: 1.05;
  }
  .contents-tab {
    position: absolute;
    bottom: 0;
    left: 50%;
    transform: translateX(-50%);
    width: 380px;
    height: 78px;
    background: var(--tab);
    border-radius: 14px 14px 0 0;
    display: flex;
    align-items: center;
    justify-content: center;
    gap: 10px;
    font-weight: 600;
    font-size: 24px;
    color: var(--white);
  }
  .contents-tab .divider {
    width: 2px;
    height: 28px;
    background: var(--cyan);
  }
</style>
</head>
<body>
  <main class="label">
    <div class="head-backdrop" role="img" aria-label="Faint outline of a head in profile with circuit lines"></div>
    <div class="network left" role="img" aria-label="Faint gold network of connected dots"></div>
    <div class="network right" role="img" aria-label="Faint gold network of connected dots"></div>

    <header class="brand-tab">
      <span class="brand-name">PURAVETA</span>
      <span class="brand-dot"></span>
    </header>

    <section class="content">
      <h1 class="product-name">DORMALUX</h1>
      <p class="claim">FÖRDERT DIE TIEFSCHLAFPHASE</p>
      <ul class="benefits">
        <li>UNTERTITEL HINZUFÜGEN</li>
        <li>UNTERTITEL HINZUFÜGEN</li>
        <li>UNTERTITEL HINZUFÜGEN</li>
      </ul>
    </section>

    <footer class="contents-tab">
      <span>30 PORTIONEN</span>
      <span class="divider"></span>
      <span>60 KAPSELN</span>
    </footer>
  </main>
</body>
</html>
```